'Tarvel' a financial/crypto-currency exchange in the middle east

On the card we need 1) Name 2) title 3) email address 4) phone number using the same colors and theme as the logo. On one side we just want the logo and we want the whole card to be in blue (same blue as logo) with the logo in the back being white.
Industry/Entity Type
Financial

```html
<!DOCTYPE html>
<html lang="en">
<head>
<meta charset="utf-8">
<title>Tarvel Business Card</title>
<link rel="stylesheet" href="https://fonts.googleapis.com/css2?family=Questrial&display=swap">
<style>
  :root {
    --brand-blue: #0e8dc9;
    --card-white: #ffffff;
    --backdrop: #e8e7e7;
    --shadow: rgba(0, 0, 0, 0.18);
  }
  * { margin: 0; padding: 0; box-sizing: border-box; }
  html, body {
    width: 1200px;
    height: 900px;
    overflow: hidden;
    background: var(--backdrop);
    font-family: "Questrial", sans-serif;
  }
  .canvas {
    position: relative;
    width: 1200px;
    height: 900px;
  }
  .card {
    position: absolute;
    left: 250px;
    width: 700px;
    height: 400px;
    border-radius: 30px;
    overflow: hidden;
    box-shadow: 0 10px 24px var(--shadow);
  }
  /* Back side: full blue with white mark */
  .card-back {
    top: 40px;
    background: var(--brand-blue);
  }
  .card-back .brand-disc {
    position: absolute;
    left: -150px;
    top: -190px;
    width: 480px;
    height: 480px;
    border-radius: 50%;
    background: var(--card-white);
  }
  .card-back .brand-name {
    position: absolute;
    right: 60px;
    bottom: 70px;
    color: var(--card-white);
    font-size: 104px;
    letter-spacing: 1px;
    line-height: 1;
  }
  /* Front side: white with contact details */
  .card-front {
    top: 470px;
    background: var(--card-white);
    color: var(--brand-blue);
  }
  .brand-lockup {
    position: absolute;
    right: 56px;
    top: 56px;
    display: flex;
    align-items: center;
    gap: 16px;
  }
  .brand-lockup .brand-dot {
    width: 72px;
    height: 72px;
    border-radius: 50%;
    background: var(--brand-blue);
  }
  .brand-lockup .brand-name {
    font-size: 62px;
    line-height: 1;
  }
  .person {
    position: absolute;
    left: 56px;
    top: 170px;
  }
  .person .name {
    font-size: 32px;
    line-height: 1.1;
  }
  .person .title {
    font-size: 18px;
    margin-top: 2px;
  }
  .contact-row {
    position: absolute;
    left: 56px;
    right: 40px;
    bottom: 56px;
    display: flex;
    align-items: center;
    gap: 14px;
    font-size: 18px;
    white-space: nowrap;
  }
  .contact-item {
    display: flex;
    align-items: center;
    gap: 6px;
  }
  .contact-item svg {
    width: 18px;
    height: 18px;
    fill: var(--brand-blue);
    stroke: var(--brand-blue);
  }
  .divider {
    font-size: 18px;
  }
</style>
</head>
<body>
<main class="canvas">

  <section class="card card-back" aria-label="Card back">
    <div class="brand-disc"></div>
    <div class="brand-name">Tarvel</div>
  </section>

  <section class="card card-front" aria-label="Card front">
    <div class="brand-lockup">
      <div class="brand-dot"></div>
      <div class="brand-name">Tarvel</div>
    </div>

    <div class="person">
      <div class="name">Your Name</div>
      <div class="title">Job Title</div>
    </div>

    <div class="contact-row">
      <span class="contact-item">
        <svg viewBox="0 0 24 24" aria-hidden="true">
          <path stroke="none" d="M6.6 10.8a15.1 15.1 0 0 0 6.6 6.6l2.2-2.2a1 1 0 0 1 1-.25 11.4 11.4 0 0 0 3.6.57 1 1 0 0 1 1 1V20a1 1 0 0 1-1 1A17 17 0 0 1 3 4a1 1 0 0 1 1-1h3.5a1 1 0 0 1 1 1c0 1.25.2 2.45.57 3.57a1 1 0 0 1-.25 1z"/>
        </svg>
        000 000 0000
      </span>
      <span class="divider">/</span>
      <span class="contact-item">
        <svg viewBox="0 0 24 24" aria-hidden="true">
          <rect x="2" y="5" width="20" height="14" rx="1" stroke="none"/>
          <path d="M3 6l9 7 9-7" fill="none" stroke="#ffffff" stroke-width="1.6"/>
        </svg>
        Youremail@xyz.com
      </span>
      <span class="divider">/</span>
      <span class="contact-item">
        <svg viewBox="0 0 24 24" aria-hidden="true">
          <g fill="none" stroke-width="1.6">
            <circle cx="12" cy="12" r="9"/>
            <ellipse cx="12" cy="12" rx="4" ry="9"/>
            <path d="M3 12h18M5 7h14M5 17h14"/>
          </g>
        </svg>
        www.yourwebsite.com
      </span>
    </div>
  </section>

</main>
</body>
</html>
```